Indy Film Production Company/Studio

We need a business card designed from an existing logo. We are a digital studio/production company that caters to creating genre entertainment, like Action, Horror, and martial arts. The card along with the logo will be used to Brand the company from letter heads to banners. The design will also be used for postcards and Brochures. It should be professional and masculine.
Updates

Thank you to all the designers who have participated. I'm narrowing down who it will be. Thank you again.

Target Market(s)

Investors, Networks, Producers, and actors

Industry/Entity Type

Film Production

Contact Information for Business Card

Benedict Harlowe
Producer/Writer/Director
www.pelvarmotionworks.com

Requirements
Must have
• Website address, Facebook icon and Twitter icon possibly in the back of the card.
Nice to have
• Logline of Company: Follow The Action.

```html
<!DOCTYPE html>
<html lang="en">
<head>
<meta charset="utf-8">
<title>Pelvar Motion Works – Business Card</title>
<link href="https://fonts.googleapis.com/css2?family=Questrial&display=swap" rel="stylesheet">
<style>
  :root {
    --stage: #2e2b29;
    --card-dark: #1c1c1d;
    --card-light: #f4f4f4;
    --ink-light: #d6d6d6;
    --ink-muted: #a9a9a9;
    --ink-dark: #1a1a1a;
    --ink-soft: #3a3a3a;
    --camera-deep: #2a2a2a;
    --camera-mid: #6d6d6d;
  }
  * { margin: 0; padding: 0; box-sizing: border-box; }
  html, body {
    width: 1200px; height: 727px; overflow: hidden;
    background: var(--stage);
    font-family: "Questrial", "Century Gothic", sans-serif;
  }
  .canvas { position: relative; width: 1200px; height: 727px; }
  .card {
    position: absolute; top: 220px; width: 500px; height: 286px;
    box-shadow: 0 14px 30px rgba(0,0,0,.45);
  }
  .card--back { left: 60px; background: var(--card-dark); color: var(--ink-light); }
  .card--front { left: 640px; background: var(--card-light); color: var(--ink-dark); overflow: hidden; }

  .back-mark {
    position: absolute; left: 0; right: 0; top: 46px; text-align: center;
  }
  .back-mark__initials { font-size: 96px; letter-spacing: 6px; line-height: 1; color: var(--ink-light); }
  .back-mark__name { margin-top: 6px; font-size: 19px; letter-spacing: 3px; text-transform: uppercase; color: var(--ink-light); }
  .back-web { margin-top: 12px; font-size: 15px; color: var(--ink-muted); letter-spacing: .5px; }
  .social { position: absolute; right: 22px; bottom: 20px; display: flex; gap: 8px; }
  .social__box { width: 24px; height: 24px; background: var(--ink-light); border-radius: 3px; }

  .front-mark { position: absolute; left: 30px; top: 30px; }
  .front-mark__initials { font-size: 52px; letter-spacing: 3px; line-height: 1; }
  .front-mark__name { font-size: 11px; letter-spacing: 1.5px; text-transform: uppercase; margin-top: 2px; }
  .person { position: absolute; left: 30px; top: 142px; }
  .person__name { font-size: 22px; }
  .person__role { font-size: 14px; color: var(--ink-soft); margin-top: 2px; }
  .contact { position: absolute; left: 30px; top: 200px; font-size: 14px; }
  .contact__line { display: flex; align-items: center; gap: 6px; margin-bottom: 8px; }
  .contact__line svg { width: 14px; height: 14px; fill: var(--ink-dark); }
  .camera {
    position: absolute; right: 0; bottom: 0; width: 210px; height: 170px;
    background: radial-gradient(ellipse at 55% 60%, var(--camera-mid), var(--camera-deep) 55%, var(--card-light) 75%);
  }
</style>
</head>
<body>
<main class="canvas">
  <section class="card card--back">
    <div class="back-mark">
      <div class="back-mark__initials">PMW</div>
      <div class="back-mark__name">Pelvar Motion Works</div>
      <div class="back-web">www.pelvarmotionworks.com</div>
    </div>
    <div class="social" aria-label="Social media">
      <span class="social__box"></span>
      <span class="social__box"></span>
      <span class="social__box"></span>
    </div>
  </section>

  <section class="card card--front">
    <div class="front-mark">
      <div class="front-mark__initials">PMW</div>
      <div class="front-mark__name">Pelvar Motion Works</div>
    </div>
    <div class="person">
      <div class="person__name">Benedict Harlowe</div>
      <div class="person__role">Producer/Writer/Director</div>
    </div>
    <div class="contact">
      <div class="contact__line">
        <svg viewBox="0 0 16 16"><path d="M3 1h3l1.5 4-2 1.2a9 9 0 0 0 4.3 4.3L11 8.5l4 1.5v3a2 2 0 0 1-2 2A13 13 0 0 1 1 3a2 2 0 0 1 2-2z"/></svg>
        <span>000 000 0000</span>
      </div>
      <div class="contact__line">
        <svg viewBox="0 0 16 16"><path d="M1 3h14v10H1z M1 3l7 6 7-6" fill="none" stroke="#1a1a1a" stroke-width="1.5"/></svg>
        <span>hello@pelvarmotionworks.com</span>
      </div>
    </div>
    <div class="camera" role="img" aria-label="Photo of a professional cinema camera rig"></div>
  </section>
</main>
</body>
</html>
```